Tello Haulage Junk Removal Postcard

I am looking to have a postcard made for my junk removal company. Details:
size: 6"x9"
I would like to keep it clean and simple. Our company colors are pink, blue and white. You can find the colors and info on the company and what we do on our website which is www.tellohaulage.example .
I've attached a sample of a postcard that was made on ArtHive for another junk removal company. I like the way the attached one looks.

```html
<!DOCTYPE html>
<html lang="en">
<head>
<meta charset="utf-8">
<title>Tello Haulage Junk Removal Postcard</title>
<link rel="stylesheet" href="https://fonts.googleapis.com/css2?family=Montserrat:ital,wght@0,400;0,600;0,800;1,400;1,600;1,800;1,900&family=Oswald:wght@700&family=Poppins:wght@400;500&display=swap">
<style>
  :root {
    --pink: #e8157f;
    --blue: #1d62b3;
    --blue-deep: #1f4f8f;
    --navy: #143a6b;
    --white: #ffffff;
    --ink: #1a1a1a;
    --stage: #ececec;
  }
  * { margin: 0; padding: 0; box-sizing: border-box; }
  html, body { width: 1200px; height: 2400px; overflow: hidden; background: var(--stage); }
  body { position: relative; font-family: "Poppins", sans-serif; }

  .card { position: absolute; left: 60px; width: 1080px; height: 722px; overflow: hidden; box-shadow: 0 4px 14px rgba(0,0,0,.18); background: var(--white); }
  .card--front { top: 330px; }
  .card--back { top: 1300px; }
  .card__inner { position: absolute; left: 0; top: 0; width: 912px; height: 610px; transform: scale(1.1842); transform-origin: 0 0; }
  .card__shapes { position: absolute; inset: 0; width: 912px; height: 610px; }
  .abs { position: absolute; white-space: nowrap; }

  /* front */
  .relax { left: 45px; top: 26px; font: italic 400 34px "Montserrat", sans-serif; color: var(--white); }
  .headline { font: 700 64px/1 "Oswald", sans-serif; font-style: italic; letter-spacing: -1px; }
  .headline--top { left: 52px; top: 82px; color: var(--white); }
  .headline--bottom { left: 42px; top: 162px; color: var(--pink); font-size: 68px; }
  .tagline { left: 45px; font: italic 400 30px/1 "Montserrat", sans-serif; color: var(--white); }
  .tagline b { font-weight: 900; }
  .tagline--one { top: 258px; }
  .tagline--two { top: 292px; left: 40px; }
  .point { left: 45px; top: 336px; font: italic 700 26px/36px "Oswald", sans-serif; color: var(--blue); letter-spacing: -.2px; }
  .service { left: 85px; font: 400 13.5px/16px "Montserrat", sans-serif; color: var(--white); white-space: normal; }
  .service--items { top: 390px; width: 290px; }
  .service--piles { top: 465px; width: 260px; }
  .service-icon { left: 32px; width: 40px; height: 32px; }

  .support { left: 42px; top: 505px; display: flex; align-items: center; gap: 6px; }
  .support__pill { display: flex; align-items: center; gap: 6px; background: var(--pink); border: 2px solid var(--white); border-radius: 22px; padding: 2px 10px; height: 40px; font: italic 900 30px "Montserrat", sans-serif; color: var(--white); }
  .support__label { font: italic 900 17px/18px "Montserrat", sans-serif; color: var(--white); }
  .support__label span { display: block; background: var(--pink); padding: 0 4px; }

  .perk { width: 70px; height: 70px; border-radius: 50%; background: var(--blue); border: 3px solid var(--white); box-shadow: 0 0 0 2px var(--pink); display: flex; align-items: center; justify-content: center; text-align: center; font: italic 400 9px/11px "Montserrat", sans-serif; color: var(--white); white-space: normal; top: 488px; }

  .free { left: 690px; width: 222px; text-align: center; color: var(--white); font-family: "Montserrat", sans-serif; font-style: italic; }
  .free--title { top: 476px; font-weight: 900; font-size: 36px; line-height: 1; }
  .free--sub { top: 514px; font-weight: 800; font-size: 21px; }
  .free--note { top: 543px; font-weight: 600; font-size: 11.5px; }

  .bar-text { font: italic 800 22px "Montserrat", sans-serif; color: var(--white); }
  .bar-phone { left: 142px; top: 573px; }
  .bar-web { left: 447px; top: 576px; font-size: 18px; }

  .brand { display: flex; align-items: center; gap: 8px; font: 800 24px "Montserrat", sans-serif; color: var(--pink); }
  .brand__dot { width: 22px; height: 22px; border-radius: 50%; background: var(--blue); }
  .brand--front { left: 722px; top: 38px; }
  .brand--back { left: 700px; top: 52px; }

  .social { width: 26px; height: 26px; border-radius: 50%; }
  .social--front { background: var(--white); top: 579px; }
  .social--back { border: 1.5px solid var(--ink); top: 583px; }

  /* back */
  .section-title { left: 55px; font: 400 20px "Montserrat", sans-serif; color: var(--white); }
  .section-title b { font-weight: 800; }
  .intro { left: 57px; top: 74px; font: 400 14.5px/21px "Montserrat", sans-serif; color: var(--white); }
  .check { font: 400 15px "Montserrat", sans-serif; color: var(--white); display: flex; align-items: center; gap: 12px; }
  .check svg { width: 18px; height: 18px; }
  .reach { left: 72px; top: 338px; font: 500 16px/22px "Poppins", sans-serif; color: var(--blue); }
  .reach-name { left: 72px; top: 380px; font: italic 900 27px "Montserrat", sans-serif; color: var(--pink); }
  .support--back { left: 80px; top: 440px; }
  .back-phone { left: 78px; top: 496px; display: flex; align-items: center; gap: 10px; font: italic 900 30px "Montserrat", sans-serif; color: var(--blue); }
  .back-web { left: 55px; top: 560px; font: italic 800 20px "Montserrat", sans-serif; color: var(--white); }
</style>
</head>
<body>

<!-- FRONT -->
<section class="card card--front" aria-label="Postcard front">
  <div class="card__inner">
    <svg class="card__shapes" viewBox="0 0 912 610">
      <defs>
        <linearGradient id="photoTone" x1="0" y1="0" x2="1" y2="1">
          <stop offset="0" stop-color="#c9ccd2"/>
          <stop offset=".55" stop-color="#8d939c"/>
          <stop offset="1" stop-color="#3d4a6e"/>
        </linearGradient>
      </defs>
      <rect width="912" height="610" fill="var(--blue)"/>
      <g role="img" aria-label="Photo of a white box truck with two smiling workers in blue overalls holding a mop and a vacuum cleaner, warehouse behind">
        <polygon points="390,0 912,0 912,460 370,460 495,245" fill="url(#photoTone)"/>
      </g>
      <polygon points="372,0 390,0 495,245 370,460 352,460 477,245" fill="var(--pink)"/>
      <polygon points="352,0 372,0 477,245 352,460 334,460 459,245" fill="var(--blue)"/>
      <polygon points="655,0 690,0 730,105 695,105" fill="var(--pink)"/>
      <polygon points="690,0 912,0 912,105 730,105" fill="var(--white)"/>
      <polygon points="0,77 385,77 410,158 0,158" fill="var(--pink)"/>
      <polygon points="0,158 440,158 465,238 0,238" fill="var(--white)"/>
      <polygon points="0,252 460,252 430,332 0,332" fill="var(--pink)"/>
      <polygon points="0,332 395,332 375,375 0,375" fill="var(--white)"/>
      <polygon points="330,475 690,475 670,565 300,565" fill="var(--white)"/>
      <polygon points="695,455 912,455 912,570 660,570" fill="var(--blue)"/>
      <polygon points="690,455 700,455 665,570 655,570" fill="var(--pink)"/>
      <rect y="570" width="912" height="40" fill="var(--navy)"/>
      <g transform="translate(108,578)" fill="none" stroke="var(--white)" stroke-width="1.6">
        <circle cx="12" cy="12" r="11"/>
        <path d="M8 6 l3 3 -1.5 2 q1.5 3 3 4 l2 -1.5 3 3 -2 2 q-6 -1 -9.5 -9.5z" fill="var(--white)" stroke="none"/>
      </g>
      <g transform="translate(414,580)" fill="none" stroke="var(--white)" stroke-width="1.4">
        <circle cx="10" cy="10" r="9"/>
        <ellipse cx="10" cy="10" rx="4" ry="9"/>
        <line x1="1" y1="10" x2="19" y2="10"/>
      </g>
    </svg>

    <div class="abs brand brand--front"><span>Tello Haulage</span><span class="brand__dot"></span></div>

    <div class="abs relax">Relax.</div>
    <div class="abs headline headline--top">WE DO THE</div>
    <div class="abs headline headline--bottom">DIRTY WORK</div>
    <div class="abs tagline tagline--one"><b>REMOVE</b> The Junk</div>
    <div class="abs tagline tagline--two"><b>RECLAIM</b> Your Space</div>
    <div class="abs point">All Your Have To Do Is Point</div>

    <svg class="abs service-icon" style="top:398px" viewBox="0 0 40 32" fill="none" stroke="var(--white)" stroke-width="1.5">
      <rect x="14" y="2" width="16" height="26"/><line x1="22" y1="2" x2="22" y2="28"/>
      <rect x="3" y="14" width="12" height="12"/><line x1="5" y1="26" x2="5" y2="30"/><line x1="28" y1="28" x2="28" y2="31"/>
    </svg>
    <p class="abs service service--items">Furniture, appliances, estate cleanout, construction debris, rental &amp; foreclosure cleanout, senior downsizing, e-Waste recycling</p>

    <svg class="abs service-icon" style="top:462px" viewBox="0 0 40 32" fill="none" stroke="var(--white)" stroke-width="1.5">
      <path d="M3 14 L20 3 L37 14"/><path d="M7 12 V29 H33 V12"/><rect x="12" y="18" width="16" height="8"/>
    </svg>
    <p class="abs service service--piles">Junk piles in attics, garages, sheds and storage units</p>

    <div class="abs support">
      <div class="support__pill">24/7
        <svg width="30" height="30" viewBox="0 0 30 30" fill="none" stroke="var(--white)" stroke-width="2.4"><circle cx="15" cy="15" r="12"/><path d="M15 8 V15 H21"/></svg>
      </div>
      <div class="support__label">Customer<span>Services</span></div>
    </div>

    <div class="abs perk" style="left:334px">Call us<br>Today</div>
    <div class="abs perk" style="left:422px">Same<br>day<br>Service</div>
    <div class="abs perk" style="left:510px">First professional experience &amp; reliable</div>
    <div class="abs perk" style="left:598px">Best Price Guarrenteed</div>

    <div class="abs free free--title">FREE</div>
    <div class="abs free free--sub">Estimates</div>
    <div class="abs free free--note">Provided prior to item removal</div>

    <div class="abs bar-text bar-phone">555-014-7328</div>
    <div class="abs bar-text bar-web">www.tellohaulage.example .</div>
    <div class="abs social social--front" style="left:800px"></div>
    <div class="abs social social--front" style="left:840px"></div>
  </div>
</section>

<!-- BACK -->
<section class="card card--back" aria-label="Postcard back">
  <div class="card__inner">
    <svg class="card__shapes" viewBox="0 0 912 610">
      <defs>
        <linearGradient id="wheelTone" x1="0" y1="0" x2="0" y2="1">
          <stop offset="0" stop-color="#d5d7db"/>
          <stop offset="1" stop-color="#6d7279"/>
        </linearGradient>
      </defs>
      <rect width="912" height="610" fill="var(--white)"/>
      <g role="img" aria-label="Black and white photo of discarded bicycles and scrap in a pile">
        <polygon points="455,320 600,320 665,610 400,610" fill="url(#wheelTone)"/>
      </g>
      <polygon points="600,320 615,320 680,610 665,610" fill="var(--blue)"/>
      <polygon points="0,0 615,0 410,610 0,610" fill="var(--blue-deep)"/>
      <polygon points="615,0 632,0 427,610 410,610" fill="var(--blue)"/>
      <polygon points="634,0 648,0 546,305 532,305" fill="var(--pink)"/>
      <line x1="55" y1="67" x2="570" y2="67" stroke="var(--white)" stroke-opacity=".6"/>
      <line x1="55" y1="165" x2="520" y2="165" stroke="var(--white)" stroke-opacity=".6"/>
      <line x1="55" y1="268" x2="505" y2="268" stroke="var(--white)" stroke-opacity=".6"/>
      <polygon points="0,328 495,328 470,415 0,415" fill="var(--white)"/>
      <polygon points="0,428 462,428 432,530 0,530" fill="var(--white)"/>
      <polygon points="0,545 400,545 378,610 0,610" fill="var(--pink)"/>
      <rect x="770" y="137" width="85" height="110" fill="none" stroke="var(--ink)" stroke-width="1.5"/>
      <g stroke="var(--ink)" stroke-width="1.2">
        <line x1="620" y1="312" x2="875" y2="312"/>
        <line x1="620" y1="367" x2="875" y2="367"/>
        <line x1="620" y1="427" x2="875" y2="427"/>
      </g>
    </svg>

    <div class="abs brand brand--back"><span>Tello Haulage</span><span class="brand__dot"></span></div>

    <div class="abs section-title" style="top:38px">JUNC REMOVAL <b>SERVICES</b></div>
    <p class="abs intro">Junk, clutter, debris, rubbish, trash, hogwash, garbage and scrap...<br>whatever you’re under, we’re here to help clean it out.</p>

    <div class="abs section-title" style="top:136px">WHY <b>CHOOSE</b></div>
    <div class="abs check" style="left:52px;top:174px"><svg viewBox="0 0 18 18" fill="none" stroke="var(--white)" stroke-width="1.4"><circle cx="9" cy="9" r="8"/><path d="M5 9 l3 3 5-6"/></svg>On time service</div>
    <div class="abs check" style="left:52px;top:199px"><svg viewBox="0 0 18 18" fill="none" stroke="var(--white)" stroke-width="1.4"><circle cx="9" cy="9" r="8"/><path d="M5 9 l3 3 5-6"/></svg>Full service junc removal</div>
    <div class="abs check" style="left:305px;top:174px"><svg viewBox="0 0 18 18" fill="none" stroke="var(--white)" stroke-width="1.4"><circle cx="9" cy="9" r="8"/><path d="M5 9 l3 3 5-6"/></svg>Upfront Pricing</div>
    <div class="abs check" style="left:305px;top:199px"><svg viewBox="0 0 18 18" fill="none" stroke="var(--white)" stroke-width="1.4"><circle cx="9" cy="9" r="8"/><path d="M5 9 l3 3 5-6"/></svg>Responsible Disposal</div>

    <div class="abs section-title" style="top:240px">OUR <b>CORE SERVICES</b></div>
    <div class="abs check" style="left:55px;top:274px"><svg viewBox="0 0 18 18" fill="var(--white)"><circle cx="9" cy="9" r="5"/><path d="M8 1h2v4H8zM8 13h2v4H8zM1 8h4v2H1zM13 8h4v2h-4z"/></svg>Residential</div>
    <div class="abs check" style="left:55px;top:297px"><svg viewBox="0 0 18 18" fill="var(--white)"><circle cx="9" cy="9" r="5"/><path d="M8 1h2v4H8zM8 13h2v4H8zM1 8h4v2H1zM13 8h4v2h-4z"/></svg>Curbside</div>
    <div class="abs check" style="left:204px;top:274px"><svg viewBox="0 0 18 18" fill="var(--white)"><circle cx="9" cy="9" r="5"/><path d="M8 1h2v4H8zM8 13h2v4H8zM1 8h4v2H1zM13 8h4v2h-4z"/></svg>Commercial</div>
    <div class="abs check" style="left:204px;top:297px"><svg viewBox="0 0 18 18" fill="var(--white)"><circle cx="9" cy="9" r="5"/><path d="M8 1h2v4H8zM8 13h2v4H8zM1 8h4v2H1zM13 8h4v2h-4z"/></svg>Other</div>
    <div class="abs check" style="left:360px;top:274px"><svg viewBox="0 0 18 18" fill="var(--white)"><circle cx="9" cy="9" r="5"/><path d="M8 1h2v4H8zM8 13h2v4H8zM1 8h4v2H1zM13 8h4v2h-4z"/></svg>Outside</div>

    <p class="abs reach">Removing junk for residential + commercial<br>clients across Northern VA through</p>
    <div class="abs reach-name">TELLO HAULAGE</div>

    <div class="abs support support--back">
      <div class="support__pill">24/7
        <svg width="30" height="30" viewBox="0 0 30 30" fill="none" stroke="var(--white)" stroke-width="2.4"><circle cx="15" cy="15" r="12"/><path d="M15 8 V15 H21"/></svg>
      </div>
      <div class="support__label"><span style="background:none;color:var(--blue);padding:0">Customer</span><span style="color:var(--white)">Services</span></div>
    </div>

    <div class="abs back-phone">
      <svg width="28" height="28" viewBox="0 0 24 24" fill="none" stroke="var(--blue)" stroke-width="1.6"><circle cx="12" cy="12" r="11"/><path d="M8 6 l3 3 -1.5 2 q1.5 3 3 4 l2 -1.5 3 3 -2 2 q-6 -1 -9.5 -9.5z" fill="var(--blue)" stroke="none"/></svg>
      555-014-7328
    </div>

    <div class="abs back-web">www.tellohaulage.example .</div>

    <div class="abs social social--back" style="left:796px"></div>
    <div class="abs social social--back" style="left:836px"></div>
  </div>
</section>

</body>
</html>
```